Ice cream manufacturer need packaging design

We are a artisanal ice cream maker - Gelato makers - we are in the process of commercialising our products to restaurants, hotels. catering services and large supermarkets. It is a unique product which we are bringing to the market as it is a traditionally made ice cream using fresh ingredients rather than flavouring. We will be selling our products in small individual containers of 100ml as well as family boxes of 500ml and 1l. A little bit like Brellovin.We need the packaging to ooze quality, it needs to scream that' this is not your average industrial air full ice cream, but quality natural ingredients'The packaging needs to include:- The brand name Plenta as a nice logo- The flavour- Ingredients section.- Batch number- Expire date (should read see lid)- The name and address of the manufacturer - Sweet Harbor, Rue Kamel Ferhani, Draria, Alger, Algerie - Special storage conditions - To be stored at -18 degrees and left at room temperature for 10 min before consumption.- Net weight: 100ml or 500ml or 1l

Industry/Entity Type

Food Production

Colors

Designer to choose colors to be used in the design.

Requirements
Must have
• Brand Name and Flavour with some reference to ice cream.
Nice to have
• It must convey that this is a quality product.
Should not have
• It should not have a funny or playful message

```html
<!DOCTYPE html>
<html lang="en">
<head>
<meta charset="utf-8">
<title>Plenta Strawberry – 100ml Tub Label</title>
<link href="https://fonts.googleapis.com/css2?family=Courgette&family=Open+Sans:wght@400;600;700&display=swap" rel="stylesheet">
<style>
  :root {
    --bg-dark: #141414;
    --bg-mid: #232323;
    --pink: #f0a3b5;
    --pink-light: #f6b9c8;
    --berry-red: #b3171f;
    --leaf-green: #3f8a2a;
    --gold-1: #8a5a1c;
    --gold-2: #f3d27a;
    --white: #ffffff;
    --ink: #1a1a1a;
    --cream: #efd3d4;
  }
  * { margin: 0; padding: 0; box-sizing: border-box; }
  html, body { width: 1200px; height: 533px; overflow: hidden; background: var(--bg-dark); }
  .label {
    position: relative;
    width: 1200px;
    height: 533px;
    overflow: hidden;
    background: radial-gradient(ellipse at 50% 40%, var(--bg-mid), var(--bg-dark) 75%);
    font-family: "Open Sans", Arial, sans-serif;
    color: var(--white);
  }
  .art {
    position: absolute;
    border-radius: 40%;
    background: radial-gradient(circle at 40% 45%, #e0303a, var(--berry-red) 60%, #6e0d12);
  }
  .art--berries-top { left: 36px; top: 48px; width: 126px; height: 68px; }
  .art--berries-bottom { left: 192px; top: 348px; width: 126px; height: 76px; }

  .story { position: absolute; left: 48px; top: 100px; width: 262px; }
  .story__title {
    font-family: "Courgette", cursive;
    font-weight: 400;
    font-size: 22px;
    text-align: right;
    padding-right: 8px;
    margin-bottom: 6px;
  }
  .story__body { font-size: 14.4px; line-height: 19.6px; text-align: justify; }

  .brand {
    position: absolute;
    left: 468px; top: 82px; width: 259px; height: 86px;
    display: flex; align-items: center; justify-content: center;
    font-family: "Courgette", cursive;
    font-size: 56px;
    color: var(--white);
  }
  .tagline {
    position: absolute; left: 366px; width: 475px; top: 196px;
    text-align: center;
    font-family: "Courgette", cursive;
    font-size: 18px;
    color: var(--pink-light);
  }
  .front-band { position: absolute; left: 366px; top: 300px; width: 475px; height: 233px; }
  .art--scoop {
    left: 456px; top: 236px; width: 168px; height: 160px; border-radius: 50%;
    background: radial-gradient(circle at 40% 40%, #f7e4e3, var(--cream) 55%, #cf8f93);
  }
  .art--strawberry {
    left: 608px; top: 240px; width: 160px; height: 156px; border-radius: 45% 45% 50% 50%;
  }
  .flavour {
    position: absolute; left: 366px; width: 475px; top: 408px;
    text-align: center;
    font-family: "Courgette", cursive;
    font-size: 52px;
    color: var(--berry-red);
  }
  .net-weight {
    position: absolute; left: 366px; width: 475px; top: 480px;
    text-align: center; font-size: 15.5px; color: var(--ink);
  }

  .info { position: absolute; left: 858px; top: 34px; width: 340px; font-size: 12.4px; line-height: 17px; }
  .info p { margin: 0; }
  .info strong { font-weight: 700; }
  .info__block--ingredients { }
  .info__dot { width: 5px; height: 5px; border-radius: 50%; background: var(--white); margin: 9px 0 9px 158px; }
  .info__block--instruction { margin-top: 0; }
  .info__block--batch { font-size: 11px; padding-left: 10px; }
  .nutrition { position: absolute; left: 858px; top: 214px; width: 340px; }
  .nutrition__title { text-align: center; font-weight: 700; font-size: 14px; margin-bottom: 8px; padding-right: 20px; }
  .nutrition__row { display: flex; gap: 7px; padding-left: 10px; }
  .nutrient {
    width: 58px; height: 86px;
    background: var(--pink);
    border: 2px solid var(--white);
    border-radius: 12px 12px 29px 29px;
    display: flex; flex-direction: column; align-items: center;
    color: var(--ink);
  }
  .nutrient__name { font-weight: 700; font-size: 12px; margin-top: 14px; }
  .nutrient__value {
    margin-top: auto; margin-bottom: 2px;
    width: 50px; height: 40px; border-radius: 50%;
    background: var(--white);
    display: flex; align-items: center; justify-content: center;
    font-weight: 700; font-size: 15px;
  }
  .nutrition__note { text-align: center; font-weight: 700; font-size: 11.5px; margin-top: 9px; padding-right: 20px; }
  .maker {
    position: absolute; left: 870px; top: 446px; width: 300px;
    text-align: center; font-size: 14.5px; line-height: 17px;
  }
</style>
</head>
<body>
<main class="label">
  <section class="side-panel">
    <div class="art art--berries-top" role="img" aria-label="Photo of two fresh strawberries"></div>
    <div class="story">
      <h2 class="story__title">Strawberry</h2>
      <p class="story__body">Dummy text is also used to show the appearance of different typefaces and layouts, and in general the content of dummy text is nonsensical. Due to its widespread use as filler text for layouts, non-readability is of great importance: human perception is tuned to recognize certain patterns and repetitions in texts.</p>
    </div>
    <div class="art art--berries-bottom" role="img" aria-label="Photo of two fresh strawberries"></div>
  </section>

  <section class="front-panel">
    <h1 class="brand">Plenta</h1>
    <p class="tagline">Glace Italienne de Qualité</p>
    <svg class="front-band" viewBox="0 0 475 233" aria-hidden="true">
      <defs>
        <linearGradient id="gold" x1="0" x2="1">
          <stop offset="0" stop-color="var(--gold-1)"/>
          <stop offset="0.45" stop-color="var(--gold-2)"/>
          <stop offset="1" stop-color="var(--gold-1)"/>
        </linearGradient>
      </defs>
      <path d="M0 92 C140 72 320 40 475 20 L475 233 L0 233 Z" fill="var(--pink)"/>
      <path d="M0 90 C150 66 320 36 475 12 L475 22 C320 46 150 76 0 94 Z" fill="url(#gold)"/>
    </svg>
    <div class="art art--scoop" role="img" aria-label="Photo of a scoop of strawberry ice cream"></div>
    <div class="art art--strawberry" role="img" aria-label="Photo of a whole fresh strawberry with leaves"></div>
    <p class="flavour">Strawberry</p>
    <p class="net-weight">Net Wt. 100ml (3.3814 oz.)</p>
  </section>

  <section class="info">
    <p class="info__block--ingredients"><strong>Ingredients:</strong> Milk, Water, Sugar, Dextrose, Strawberries, Coco Butter, Emulsifier, Stabilizers</p>
    <div class="info__dot"></div>
    <p class="info__block--instruction"><strong>Instruction:</strong> Please keep refrigerated at -18 degrees, before consuming allow 10 min to thaw.</p>
    <div class="info__dot"></div>
    <p class="info__block--batch">BATCH No &amp; EXPIRY DATE: see bottom of tub</p>
    <div class="info__dot"></div>
  </section>

  <section class="nutrition">
    <h3 class="nutrition__title">PER SERVINGS</h3>
    <div class="nutrition__row">
      <div class="nutrient"><span class="nutrient__name">Energy</span><span class="nutrient__value">20%</span></div>
      <div class="nutrient"><span class="nutrient__name">Carbs</span><span class="nutrient__value">32%</span></div>
      <div class="nutrient"><span class="nutrient__name">Fiber</span><span class="nutrient__value">28%</span></div>
      <div class="nutrient"><span class="nutrient__name">Protein</span><span class="nutrient__value">21%</span></div>
      <div class="nutrient"><span class="nutrient__name">Salt</span><span class="nutrient__value">3%</span></div>
    </div>
    <p class="nutrition__note">OF YOUR GUIDELINE DAILY AMOUNT</p>
  </section>

  <address class="maker" style="font-style: normal;">
    The Manufacturer<br>
    Sweet Harbor, Rue Kamel Ferhani,<br>
    Draria, Alger, Algerie
  </address>
</main>
</body>
</html>
```